Slide desk development general pellham stride

I am looking to expand the range of slide templates we have using our new branded powerpoint deck so the team have more options.

Target Market(s)

We operate in the construction sector

Industry/Entity Type

Construction

Requirements
Must have
• Picture linking back to construction

```html
<!DOCTYPE html>
<html lang="en">
<head>
<meta charset="utf-8">
<title>Pellham Stride – Slide Templates</title>
<link href="https://fonts.googleapis.com/css2?family=Poppins:wght@400;500;600;700;800&display=swap" rel="stylesheet">
<style>
:root{
  --black:#000;
  --ink:#111;
  --green:#9be36b;
  --grid:#2b4592;
  --panel:#2b2b2b;
  --gold:#f2c21b;
  --white:#fff;
  --sep:#cfcfcf;
  --muted:#dcdcdc;
}
*{margin:0;padding:0;box-sizing:border-box}
html,body{width:1200px;height:4792px;overflow:hidden}
body{position:relative;background:var(--sep);font-family:'Poppins',sans-serif;color:var(--white)}
.abs{position:absolute}
.section{position:absolute;left:0;width:1200px;background:var(--black)}
.photo{position:absolute}

/* Timeframe */
.timeframe{top:0;height:674px}
.timeframe h1{position:absolute;top:46px;left:0;width:1200px;text-align:center;font-size:48px;font-weight:700}
.gantt{position:absolute;left:47px;top:121px}
.gantt-note{position:absolute;left:56px;top:536px;width:1060px;font-size:13.5px;line-height:26px;color:var(--white)}

/* Hero */
.hero{top:684px;height:678px;background:linear-gradient(160deg,#5d5a52,#8c7d66 45%,#6f6a60 70%,#3e3d3a)}
.brand-pill{position:absolute;left:819px;top:1155px;width:381px;height:151px;background:#111;border-radius:76px 0 0 76px;display:flex;align-items:center;padding-left:60px;gap:18px}
.brand-mark{width:26px;height:26px;background:var(--green)}
.brand-name{font-size:34px;font-weight:500;color:var(--white);letter-spacing:.5px}

/* Current projects */
.projects{top:1373px;height:673px}
.projects .strip{position:absolute;left:0;top:0;width:56px;height:673px;background:var(--green)}
.projects h2{position:absolute;left:134px;top:96px;font-size:38px;font-weight:800;line-height:48px}
.projects .body{position:absolute;left:134px;width:300px;font-size:13px;line-height:25px}
.progress{position:absolute;width:82px;height:82px;border-radius:50%;background:var(--green);display:flex;align-items:center;justify-content:center;font-size:23px;font-weight:500}
.progress-title{position:absolute;font-size:18px;font-weight:600}
.progress-desc{position:absolute;font-size:13px;line-height:25px;width:210px}

/* Portfolio */
.portfolio-title{position:absolute;left:348px;top:2058px;width:504px;height:329px;background:var(--panel);display:flex;align-items:center;justify-content:center;font-size:46px;font-weight:500;letter-spacing:1px}
.portfolio-title span{color:var(--gold)}

/* Double contents */
.double{top:3434px;height:668px}
.double h2{position:absolute;left:69px;top:80px;font-size:35px;font-weight:700}
.card2{position:absolute;top:198px;width:462px;height:364px;padding:38px 26px 0}
.card2 h3{font-size:24px;font-weight:700;color:var(--ink);margin-bottom:26px}
.card2 p{font-size:20px;line-height:36px;color:var(--ink)}
.hex{position:absolute}

/* Six columns */
.six{top:4121px;height:671px}
.six h2{position:absolute;left:91px;top:56px;font-size:38px;font-weight:700}
.tile{position:absolute;width:324px;height:218px;padding:30px 34px 0 36px;color:var(--ink)}
.tile .head{display:flex;align-items:center;gap:24px;height:40px;margin-bottom:16px}
.tile .head svg{flex:none}
.tile h4{font-size:18px;font-weight:700}
.tile p{font-size:14px;line-height:22px}
.g{background:var(--green)}
.w{background:var(--white)}
</style>
</head>
<body>

<!-- Timeframe -->
<section class="section timeframe">
  <h1>Timeframe</h1>
  <svg class="gantt" width="1070" height="408" viewBox="0 0 1070 408" font-family="Poppins, sans-serif">
    <g stroke="var(--grid)" stroke-width="1.5" fill="none">
      <rect x="0.75" y="0.75" width="1068.5" height="405.5"/>
      <line x1="0" y1="58" x2="1069" y2="58"/>
      <line x1="0" y1="113" x2="1069" y2="113"/>
      <line x1="0" y1="234" x2="1069" y2="234"/>
      <line x1="0" y1="290" x2="1069" y2="290"/>
      <line x1="0" y1="348" x2="1069" y2="348"/>
      <line x1="145" y1="0" x2="145" y2="407"/>
      <g stroke-width="1">
        <line x1="222" y1="58" x2="222" y2="407"/><line x1="299" y1="58" x2="299" y2="407"/>
        <line x1="376" y1="58" x2="376" y2="407"/><line x1="453" y1="58" x2="453" y2="407"/>
        <line x1="530" y1="58" x2="530" y2="407"/><line x1="607" y1="58" x2="607" y2="407"/>
        <line x1="684" y1="58" x2="684" y2="407"/><line x1="761" y1="58" x2="761" y2="407"/>
        <line x1="838" y1="58" x2="838" y2="407"/><line x1="915" y1="58" x2="915" y2="407"/>
        <line x1="992" y1="58" x2="992" y2="407"/>
      </g>
    </g>
    <g fill="#fff" font-size="22" font-weight="500" text-anchor="middle">
      <text x="228" y="37">Jan</text><text x="382" y="37">Feb</text><text x="536" y="37">Mar</text>
      <text x="690" y="37">Apr</text><text x="844" y="37">May</text><text x="998" y="37">Jun</text>
    </g>
    <g fill="#fff" font-size="13">
      <text x="8" y="91">Kickoff Meeting</text>
      <text x="8" y="135">Analytics</text><text x="8" y="153">Implementations,</text>
      <text x="8" y="171">Website Audit,</text><text x="8" y="189">Content and</text>
      <text x="8" y="207">Keyword</text><text x="8" y="225">Research</text>
      <text x="8" y="258">Digital Strategy</text><text x="8" y="275">Development</text>
      <text x="8" y="315">Content</text><text x="8" y="332">Development</text>
      <text x="8" y="382">Go Live</text>
    </g>
    <g fill="var(--green)">
      <rect x="169" y="73" width="195" height="28" rx="14"/>
      <rect x="353" y="159" width="201" height="28" rx="14"/>
      <rect x="546" y="245" width="203" height="28" rx="14"/>
      <rect x="699" y="304" width="203" height="28" rx="14"/>
      <rect x="818" y="360" width="203" height="28" rx="14"/>
    </g>
  </svg>
  <p class="gantt-note">To complete the work outlined in the project scope, we'll need approximately eight weeks to the going live date, depending on feedback at each milestone. Upon signing the proposal, we are prepared to start work immediately.</p>
</section>

<!-- Hero -->
<div class="section hero" role="img" aria-label="Aerial photograph of a large construction site with cranes, scaffolding and concrete foundations"></div>
<div class="brand-pill"><span class="brand-mark"></span><span class="brand-name">pellham stride</span></div>

<!-- Current projects -->
<section class="section projects">
  <div class="strip"></div>
  <h2>CURRENT<br>PROJECTS</h2>
  <p class="body" style="top:236px">Lorem Ipsum is simply dummy text of the printing and typesetting industry. Lorem Ipsum has been the industry's standard dummy text ever since the 1500s,</p>
  <p class="body" style="top:368px">Lorem Ipsum is simply dummy text of the printing and typesetting industry. Lorem Ipsum has been the industry's standard dummy text ever since the 1500s,</p>
  <div class="photo" style="left:512px;top:0;width:273px;height:357px;background:linear-gradient(160deg,#7b7a72,#9a8a72 55%,#5e5d58)" role="img" aria-label="Aerial view of building construction with red tower cranes"></div>
  <div class="photo" style="left:811px;top:0;width:274px;height:357px;background:linear-gradient(170deg,#c08a5a,#b27a4c 50%,#a06c42)" role="img" aria-label="Aerial view of excavators and trucks on a sandy earthworks site"></div>
  <div class="progress" style="left:517px;top:402px">65%</div>
  <div class="progress" style="left:820px;top:402px">15%</div>
  <div class="progress-title" style="left:532px;top:500px">Still In Progress</div>
  <div class="progress-title" style="left:820px;top:500px">Still In Progress</div>
  <p class="progress-desc" style="left:532px;top:546px;width:170px">Lorem ipsum dolor sit amet, consectetur adipiscing elit,</p>
  <p class="progress-desc" style="left:820px;top:546px">Lorem ipsum dolor sit amet, consectetur adipiscing elit,</p>
</section>

<!-- Portfolio -->
<div class="photo" style="left:0;top:2058px;width:333px;height:329px;background:linear-gradient(180deg,#8fb6d8,#c9a27c 45%,#5d7a3c)" role="img" aria-label="Curved stucco villa above a vineyard"></div>
<div class="portfolio-title">PORT<span>FOLIO</span></div>
<div class="photo" style="left:867px;top:2058px;width:333px;height:329px;background:linear-gradient(180deg,#a9c6de,#c7b296 50%,#6d6456)" role="img" aria-label="Modern glass and timber house with cacti"></div>
<div class="photo" style="left:0;top:2398px;width:424px;height:335px;background:linear-gradient(180deg,#7aa9d9,#dfe6ee 55%,#9aa3a8)" role="img" aria-label="White curved residential towers with palm trees"></div>
<div class="photo" style="left:432px;top:2398px;width:338px;height:335px;background:linear-gradient(180deg,#9fb5c9,#e2d5c2 50%,#a08368)" role="img" aria-label="Curved white villa with terraces at dusk"></div>
<div class="photo" style="left:778px;top:2398px;width:422px;height:335px;background:linear-gradient(180deg,#3c4a3a,#8a5c34 55%,#2c2620)" role="img" aria-label="Timber and concrete house lit up at dusk in a forest"></div>
<div class="photo" style="left:0;top:2744px;width:337px;height:426px;background:linear-gradient(180deg,#4d6f93,#c99b7a 50%,#2e3a2e)" role="img" aria-label="Beachside house with palm trees at sunset"></div>
<div class="photo" style="left:346px;top:2744px;width:508px;height:426px;background:linear-gradient(180deg,#d9c7ab,#b5a189 50%,#6e7478)" role="img" aria-label="Cliffside modern villa with infinity pool at sunrise"></div>
<div class="photo" style="left:861px;top:2744px;width:339px;height:240px;background:linear-gradient(180deg,#5f9ad6,#f0f0ee 55%,#4fc4d8)" role="img" aria-label="White Mediterranean villa with turquoise pool by the sea"></div>
<div class="photo" style="left:861px;top:2992px;width:339px;height:428px;background:linear-gradient(180deg,#9bb4d6,#e6e9ee 50%,#b9c1cb)" role="img" aria-label="Tall white apartment tower against a blue sky"></div>
<div class="photo" style="left:0;top:3180px;width:337px;height:240px;background:linear-gradient(180deg,#d8c7b3,#b76e48 55%,#7d4a32)" role="img" aria-label="Terracotta adobe courtyard house with pool"></div>
<div class="photo" style="left:346px;top:3180px;width:508px;height:240px;background:linear-gradient(180deg,#6f8a6a,#7a5a3c 55%,#3b4a33)" role="img" aria-label="Contemporary timber house among trees"></div>

<!-- Double contents -->
<section class="section double">
  <h2>Double Contents</h2>
  <div class="card2" style="left:102px;background:var(--green)">
    <h3>First Content</h3>
    <p>Leverage agile frameworks to provide a robust synopsis for high level overviews. Iterative approaches to corporate strategy foster collaborative thinking to further</p>
  </div>
  <svg class="hex" style="left:454px;top:140px" width="134" height="112" viewBox="0 0 134 112">
    <polygon points="33,0 101,0 134,56 101,112 33,112 0,56" fill="#fff"/>
    <g fill="none" stroke="#111" stroke-width="3.5" stroke-linejoin="round">
      <circle cx="67" cy="56" r="10"/>
      <path d="M63 26h8l2 7 6 3 7-3 6 6-3 7 3 6 7 2v8l-7 2-3 6 3 7-6 6-7-3-6 3-2 7h-8l-2-7-6-3-7 3-6-6 3-7-3-6-7-2v-8l7-2 3-6-3-7 6-6 7 3 6-3z"/>
    </g>
  </svg>
  <div class="card2" style="left:634px;background:var(--white)">
    <h3>Second Content</h3>
    <p>Leverage agile frameworks to provide a robust synopsis for high level overviews. Iterative approaches to corporate strategy foster collaborative thinking to further</p>
  </div>
  <svg class="hex" style="left:980px;top:140px" width="136" height="112" viewBox="0 0 136 112">
    <polygon points="34,0 102,0 136,56 102,112 34,112 0,56" fill="var(--green)"/>
    <g fill="none" stroke="#fff" stroke-width="3.5" stroke-linejoin="round">
      <path d="M50 28h36v20a18 18 0 0 1-36 0z"/>
      <path d="M50 34H40a12 12 0 0 0 12 16M86 34h10a12 12 0 0 1-12 16"/>
      <path d="M68 66v12M56 86h24v-8H56z"/>
      <path d="M68 36l3 6 6 1-5 4 1 6-5-3-5 3 1-6-5-4 6-1z"/>
    </g>
  </svg>
</section>

<!-- Six columns -->
<section class="section six">
  <h2>Six Column Content</h2>
  <div class="tile g" style="left:82px;top:139px">
    <div class="head"><svg width="42" height="42" viewBox="0 0 42 42" fill="none" stroke="#111" stroke-width="2.5"><circle cx="21" cy="21" r="18"/><path d="M26 14h-7a4 4 0 0 0 0 8h4a4 4 0 0 1 0 8h-8M21 10v4M21 30v3"/></svg><h4>Number One</h4></div>
    <p>Leverage agile frameworks to provide a robust synopsis for high level overviews. Iterative approaches to corporate strategy foster collaborative thinking to.</p>
  </div>
  <div class="tile w" style="left:452px;top:139px">
    <div class="head"><svg width="42" height="42" viewBox="0 0 42 42" fill="none" stroke="#111" stroke-width="2.5" stroke-linejoin="round"><path d="M36 6c-10 0-18 6-22 16l6 6c10-4 16-12 16-22z"/><circle cx="27" cy="15" r="3"/><path d="M14 22l-7 1 4-7h8M20 28l-1 7 7-4v-8M12 30l-6 6"/></svg><h4>Number Two</h4></div>
    <p>Leverage agile frameworks to provide a robust synopsis for high level overviews. Iterative approaches to corporate strategy foster collaborative thinking to.</p>
  </div>
  <div class="tile g" style="left:822px;top:139px">
    <div class="head"><svg width="42" height="42" viewBox="0 0 42 42" fill="none" stroke="#111" stroke-width="2.5" stroke-linejoin="round"><path d="M4 6h34M7 6v22h28V6M21 28v6M14 38l7-4 7 4M12 22l7-7 5 4 7-8"/></svg><h4>Number Three</h4></div>
    <p>Leverage agile frameworks to provide a robust synopsis for high level overviews. Iterative approaches to corporate strategy foster collaborative thinking to.</p>
  </div>
  <div class="tile w" style="left:82px;top:391px">
    <div class="head"><svg width="42" height="42" viewBox="0 0 42 42" fill="none" stroke="#111" stroke-width="2.5" stroke-linejoin="round"><path d="M18 8a16 16 0 1 0 16 16H18z"/><path d="M23 3v16h16A16 16 0 0 0 23 3z"/></svg><h4>I am Four</h4></div>
    <p>Leverage agile frameworks to provide a robust synopsis for high level overviews. Iterative approaches to corporate strategy foster collaborative thinking to.</p>
  </div>
  <div class="tile g" style="left:452px;top:391px">
    <div class="head"><svg width="42" height="42" viewBox="0 0 42 42" fill="none" stroke="#111" stroke-width="2.5" stroke-linecap="round"><circle cx="21" cy="24" r="15"/><path d="M16 4h10M21 4v5M21 24l6-6M7 10l4 4M35 10l-4 4"/></svg><h4>Me Number Five</h4></div>
    <p>Leverage agile frameworks to provide a robust synopsis for high level overviews. Iterative approaches to corporate strategy foster collaborative thinking to.</p>
  </div>
  <div class="tile w" style="left:822px;top:391px">
    <div class="head"><svg width="42" height="42" viewBox="0 0 42 42" fill="none" stroke="#111" stroke-width="2.5" stroke-linejoin="round"><path d="M21 4a13 13 0 0 0-8 23v5h16v-5a13 13 0 0 0-8-23z"/><path d="M15 37h12M21 14l-4 7h8l-4 7"/></svg><h4>I am Six</h4></div>
    <p>Leverage agile frameworks to provide a robust synopsis for high level overviews. Iterative approaches to corporate strategy foster collaborative thinking to.</p>
  </div>
</section>

</body>
</html>
```